Graphics Design of Physics Book

Hi
Size : 8" x 11.25"
We are education book Publication Company and would like to have book cover for "Physics" it has 4 volumes. All 4 having the same color scheme and design except the volume no.
Blue is my personal favorite but u can use any color. Want to have a band at the bottom of the cover to place our Logo “VORLIN Education” a PDF of the same is attached, or you can place logo anywhere according to ur design.
I need “Physics” as title of the book to be visible prominently.
And volume and volume no. should also be Visible and eye catching I prefer a Graphic to enhance the Volume No.
A background pattern can also be a option (it should be vector form so that color can be change later)
Please do not offer any cut and paste design I need very professional presentation.
Volume and Number can be in metallic 3D (CMYK) effect.
only Professional presentation will get feedback.
I have provided a sample artwork for reference do not follow it but can be a reference what I needed !

Target Market(s)

Students Class 9th to 12th

Industry/Entity Type

Education

Font styles to use
Serif

Colors
3176b5
0555a3
85abd2
cadf82
abd036
9bcb3c

Requirements
Must have
• Eye catching.
• “Physics” as title of the book to be visible prominently.
• volume and volume no. should also be Visible and eye catching
• I prefer a Graphic to enhance the Volume No.
• Icons for
• 1. Questions and answers
• 2. Theory Notes
• 3. Tips & Tricks
• 4. Previous Year's Reference Questions
• 5. Covers Complete Syllabus
Nice to have
• decent seamless background or metallic 3d effect (not to be print in special Ink) design should only be in CMYK.
Should not have
• Physics related Pictures or Icons (Specially E=mc2) or any scientist photograph or I Need pure graphic design

```html
<!DOCTYPE html>
<html lang="en">
<head>
<meta charset="utf-8">
<title>Physics – Book Cover</title>
<link href="https://fonts.googleapis.com/css2?family=Oswald:wght@400;500&family=Roboto+Condensed:wght@400;700&display=swap" rel="stylesheet">
<style>
  :root {
    --navy-deep: #031a3d;
    --navy: #0a2f6b;
    --royal: #0555a3;
    --sky: #3176b5;
    --mist: #85abd2;
    --white: #ffffff;
    --ink: #111111;
  }
  * { margin: 0; padding: 0; box-sizing: border-box; }
  html, body { width: 800px; height: 1200px; overflow: hidden; background: var(--ink); }
  .cover {
    position: relative;
    width: 800px; height: 1200px;
    overflow: hidden;
    background:
      radial-gradient(ellipse 520px 420px at 560px 520px, rgba(133,171,210,0.55), transparent 70%),
      radial-gradient(ellipse 700px 500px at 380px 700px, rgba(49,118,181,0.5), transparent 75%),
      linear-gradient(180deg, var(--navy) 0%, var(--royal) 45%, var(--navy) 100%);
  }
  .top-strip { position: absolute; left: 0; top: 0; width: 800px; height: 28px; background: var(--navy-deep); }
  .title-band {
    position: absolute; left: 0; top: 28px; width: 800px; height: 300px;
    background: linear-gradient(180deg, var(--royal) 0%, var(--sky) 60%, rgba(49,118,181,0) 100%);
  }
  .rule { position: absolute; left: 0; width: 800px; height: 5px; background: var(--white); }
  .rule--top { top: 40px; }
  .rule--bottom { top: 258px; }
  .title {
    position: absolute; left: 0; top: 62px; width: 800px;
    text-align: center;
    font-family: "Oswald", sans-serif; font-weight: 500;
    font-size: 168px; line-height: 1; letter-spacing: 6px;
    color: var(--white);
  }
  .volume {
    position: absolute; left: 0; top: 268px; width: 800px;
    text-align: center;
    font-family: "Oswald", sans-serif; font-weight: 400;
    font-size: 44px; letter-spacing: 1px;
    color: var(--white);
  }
  .graphic {
    position: absolute; left: 0; top: 340px; width: 360px; height: 620px;
    background: radial-gradient(circle at 45% 50%, rgba(255,255,255,0.55), rgba(133,171,210,0.3) 45%, transparent 72%);
  }
  .features { position: absolute; left: 385px; top: 375px; list-style: none; }
  .feature {
    display: flex; align-items: center; height: 80px;
    font-family: "Roboto Condensed", sans-serif; font-weight: 400;
    font-size: 25px; line-height: 1.05; text-transform: uppercase;
    color: var(--white);
  }
  .feature svg { flex: none; width: 52px; height: 52px; margin-right: 22px; }
  .footer-band {
    position: absolute; left: 0; top: 1055px; width: 800px; height: 108px;
    background: var(--white);
    display: flex; align-items: center; justify-content: center;
  }
  .brand {
    font-family: "Roboto Condensed", sans-serif; font-weight: 700;
    font-size: 40px; letter-spacing: 2px;
    color: var(--ink);
  }
  .bottom-strip { position: absolute; left: 0; top: 1163px; width: 800px; height: 37px; background: var(--ink); }
</style>
</head>
<body>
<div class="cover">
  <div class="top-strip"></div>
  <div class="title-band"></div>
  <div class="rule rule--top"></div>
  <h1 class="title">PHYSICS</h1>
  <div class="rule rule--bottom"></div>
  <p class="volume">VOLUME NO.</p>

  <div class="graphic" role="img" aria-label="Abstract glowing white circles linked by dashed lines"></div>

  <ul class="features">
    <li class="feature">
      <svg viewBox="0 0 52 52"><circle cx="26" cy="26" r="25" fill="#fff"/><text x="26" y="35" text-anchor="middle" font-family="Oswald, sans-serif" font-size="26" font-weight="500" fill="#031a3d">?!</text></svg>
      Questions and answers
    </li>
    <li class="feature">
      <svg viewBox="0 0 52 52"><circle cx="26" cy="26" r="25" fill="#fff"/><path d="M26 11 L35 26 L29 38 H23 L17 26 Z" fill="#031a3d"/><circle cx="26" cy="27" r="2.5" fill="#fff"/><rect x="22" y="39" width="8" height="4" fill="#031a3d"/></svg>
      Theory notes
    </li>
    <li class="feature">
      <svg viewBox="0 0 52 52"><circle cx="26" cy="26" r="25" fill="#fff"/><circle cx="26" cy="23" r="9" fill="none" stroke="#031a3d" stroke-width="3"/><rect x="22" y="33" width="8" height="6" fill="#031a3d"/><path d="M26 6v4M12 12l3 3M40 12l-3 3M8 23h4M40 23h4" stroke="#031a3d" stroke-width="2.5"/></svg>
      Tips &amp; tricks
    </li>
    <li class="feature">
      <svg viewBox="0 0 52 52"><circle cx="26" cy="26" r="25" fill="#fff"/><circle cx="22" cy="24" r="11" fill="#031a3d"/><text x="22" y="30" text-anchor="middle" font-family="Oswald, sans-serif" font-size="16" fill="#fff">?</text><path d="M30 32 L38 40" stroke="#031a3d" stroke-width="4"/></svg>
      Previous year's reference<br>questions
    </li>
    <li class="feature">
      <svg viewBox="0 0 52 52"><circle cx="26" cy="26" r="25" fill="#fff"/><g fill="none" stroke="#031a3d" stroke-width="3"><path d="M13 18h26M13 25h26M13 32h26M13 39h26"/></g></svg>
      Covers complete syllabus
    </li>
  </ul>

  <div class="footer-band">
    <span class="brand">VORLIN Education</span>
  </div>
  <div class="bottom-strip"></div>
</div>
</body>
</html>
```